spoonful of caviar

I am looking to design a flyer/leaflet to distribute to houses or post on shop windows that invite people to buy caviar. The moto is: With our LOW prices you can now afford real CAVIAR by the SPOONFUL!
Customers will be offered three-four type of product or more on the website. There will be price advertised on the leaflet, brief description of the product and delivery terms: Free local delivery* (Wed & Fri, For more options: call 07700900482. The actual products are on the attached files and the theme ideas are there too.
Shop

```html
<!DOCTYPE html>
<html lang="en">
<head>
<meta charset="utf-8">
<title>Caviar by the Spoonful – Flyer</title>
<link href="https://fonts.googleapis.com/css2?family=Archivo+Black&family=Tinos&display=swap" rel="stylesheet">
<style>
  :root {
    --backdrop: #4b3b30;
    --red: #b3161c;
    --red-dark: #8a0e13;
    --red-light: #d8262c;
    --white: #ffffff;
    --yellow: #f7d21a;
    --orange: #f6a02c;
    --photo-green: #6f8f52;
    --photo-cream: #e9e1d2;
    --photo-roe: #e0541f;
    --cans-silver: #d9d4d0;
  }
  * { margin: 0; padding: 0; box-sizing: border-box; }
  html, body { width: 938px; height: 1200px; overflow: hidden; }
  body { background: var(--backdrop); position: relative; }

  .flyer {
    position: absolute; left: 42px; top: 55px;
    width: 853px; height: 1093px;
    background: var(--red); overflow: hidden;
  }
  .flyer__art { position: absolute; inset: 0; }

  .headline {
    position: absolute; left: 0; right: 0; top: 38px;
    text-align: center; font-family: "Archivo Black", sans-serif;
  }
  .headline__lead { color: var(--white); font-size: 25px; line-height: 1.1; padding-left: 70px; }
  .headline__main { color: var(--orange); font-size: 45px; line-height: 1.25; padding-left: 70px; letter-spacing: 0.5px; }

  .body-copy {
    position: absolute; left: 40px; top: 693px; width: 790px;
    font-family: "Tinos", serif; color: var(--white);
    font-size: 17.5px; line-height: 22px;
  }
  .body-copy p + p { margin-top: 22px; }

  .delivery {
    position: absolute; left: 40px; top: 928px;
    font-family: "Archivo Black", sans-serif; color: var(--yellow);
    font-size: 29px; line-height: 1;
  }
  .delivery__days {
    position: absolute; left: 108px; top: 965px;
    font-family: "Tinos", serif; color: var(--white); font-size: 17px;
  }
  .contact__label {
    position: absolute; left: 127px; top: 997px;
    font-family: "Tinos", serif; color: var(--white); font-size: 17px;
  }
  .contact__phone {
    position: absolute; left: 98px; top: 1017px;
    font-family: "Archivo Black", sans-serif; color: var(--yellow);
    font-size: 31px; letter-spacing: 1px;
  }
</style>
</head>
<body>
  <div class="flyer">
    <svg class="flyer__art" width="853" height="1093" viewBox="0 0 853 1093">
      <defs>
        <linearGradient id="dishPhoto" x1="0" y1="0" x2="0" y2="1">
          <stop offset="0" stop-color="var(--photo-green)"/>
          <stop offset="0.45" stop-color="var(--photo-cream)"/>
          <stop offset="1" stop-color="#c98a45"/>
        </linearGradient>
        <linearGradient id="spoonPhoto" x1="0" y1="0" x2="0" y2="1">
          <stop offset="0" stop-color="#cfd7e0"/>
          <stop offset="0.55" stop-color="var(--photo-roe)"/>
          <stop offset="1" stop-color="#9a8a6a"/>
        </linearGradient>
        <linearGradient id="cansPhoto" x1="0" y1="0" x2="1" y2="1">
          <stop offset="0" stop-color="var(--cans-silver)"/>
          <stop offset="0.6" stop-color="#c53a3a"/>
          <stop offset="1" stop-color="#7a4a7a"/>
        </linearGradient>
      </defs>

      <!-- hero photo area -->
      <path class="hero-photo" role="img" aria-label="Pastry cups filled with cream topped with red and black caviar, on white dishes"
            fill="url(#dishPhoto)"
            d="M40 0 H853 V545 C760 610 560 650 400 640 C230 625 100 470 40 255 Z"/>
      <!-- swoosh bands -->
      <path d="M40 255 C100 470 230 625 400 640 C560 650 760 610 853 545" fill="none" stroke="var(--white)" stroke-width="16"/>
      <path d="M20 275 C85 490 225 650 400 662 C560 672 760 632 853 570" fill="none" stroke="var(--yellow)" stroke-width="6"/>
      <path d="M0 10 C15 60 30 120 40 255" fill="none" stroke="var(--white)" stroke-width="12"/>

      <!-- spoon inset -->
      <circle cx="268" cy="527" r="139" fill="var(--yellow)"/>
      <circle cx="268" cy="527" r="131" fill="var(--white)"/>
      <circle class="spoon-photo" role="img" aria-label="Spoonful of red salmon caviar over an open tin" cx="268" cy="527" r="126" fill="url(#spoonPhoto)"/>

      <!-- lower swooshes -->
      <path d="M0 960 C250 930 560 900 853 780 V1093 H0 Z" fill="var(--red-dark)"/>
      <path d="M0 1060 C300 1050 600 1010 853 880" fill="none" stroke="var(--red-light)" stroke-width="40"/>
      <path d="M430 1093 C620 1060 760 990 853 900" fill="none" stroke="var(--white)" stroke-width="12"/>
      <path d="M470 1093 C650 1070 780 1010 853 935" fill="none" stroke="var(--yellow)" stroke-width="5"/>

      <!-- product tins -->
      <rect class="product-photo" role="img" aria-label="Three tins of Russian salmon caviar" x="468" y="825" width="365" height="225" rx="14" fill="url(#cansPhoto)"/>
    </svg>

    <div class="headline">
      <div class="headline__lead">With our low prices you can now afford real</div>
      <div class="headline__main">CAVIAR by SPOON-FULL!!!</div>
    </div>

    <div class="body-copy">
      <p>A MUST HAVE for Russian caviar lovers!!! &nbsp;It would make a delicious addition to your party or an amazing and unique gift for any Occasion, too good to miss!!!</p>
      <p>Russian caviar has long been a delicacy for thousands of people. &nbsp;Our purchasing<br>power allowed us to bring it to you at a price that would make you, your family and<br>your friends enjoy it by spoon-full. &nbsp;To impress<br>them even more, you can also buy the caviar<br>pot souvenir from my other items and keep it<br>as a reminder of delicious times!</p>
    </div>

    <div class="delivery">FREE LOCAL DELIVERY*</div>
    <div class="delivery__days">(WEDNESDAY &amp; FRIDAY)</div>
    <div class="contact__label">For more options call:</div>
    <div class="contact__phone">07700900482</div>
  </div>
</body>
</html>
```